Drifting Past Solvane website

A very basic website using the graphics provided. The site would give the user the ability to read a description of the book, read testimonials, About the author, Read chapter 1, link to vendoro, order direct via coinlet.

```html
<!DOCTYPE html>
<html lang="en">
<head>
<meta charset="utf-8">
<title>Drifting Past Solvane</title>
<link rel="stylesheet" href="https://fonts.googleapis.com/css2?family=Cinzel:wght@400&family=Carlito:ital,wght@0,400;0,700;1,400&family=Arimo:wght@400&family=Tinos:wght@700&display=swap">
<style>
:root{
  --bar:#2e2e2e;
  --black:#000;
  --white:#fff;
  --gold:#f6a800;
  --text:#7a7a7a;
  --text-dark:#444;
  --band:#f3f3f3;
  --rule:#d6d6d6;
  --link:#1a9ad6;
}
*{margin:0;padding:0;box-sizing:border-box}
html,body{width:1200px;height:1000px;overflow:hidden;background:var(--white)}
body{position:relative;font-family:"Carlito",Calibri,sans-serif;color:var(--text)}
h2,p{font-weight:400}
.abs{position:absolute}

.top-bar{left:0;top:0;width:1200px;height:35px;background:var(--bar)}
.order{left:297px;top:10px;display:flex;align-items:center;gap:8px;color:#cfcfcf;font-size:11.5px}
.order b{color:var(--white)}
.vendor{height:17px;padding:0 4px;background:var(--white);border-radius:2px;color:var(--text-dark);font-size:9px;font-weight:700;line-height:17px}
.vendor.first{margin-left:8px}
.social{right:303px;top:8px;display:flex;gap:5px}
.social span{width:19px;height:19px;border-radius:50%;background:var(--white);color:var(--bar);font-size:5.5px;font-weight:700;display:flex;align-items:center;justify-content:center}

.masthead{left:0;top:35px;width:1200px;height:91px;background:var(--black)}
.site-name{left:0;top:64px;width:1200px;text-align:center;font-family:"Carlito",Calibri,sans-serif;font-weight:400;font-size:28px;color:var(--gold);line-height:1}

.nav a{position:absolute;top:144px;font-family:"Arimo",Arial,sans-serif;font-size:9.5px;color:#555;text-decoration:none;white-space:nowrap}
.nav a.active{color:#111}

.hero{left:0;top:170px;width:1200px;height:311px;background:var(--black)}
.hero-art{left:447px;top:170px;width:388px;height:311px;background:linear-gradient(90deg,#1a0f0c 0%,#4a3a35 20%,#6fa5c6 40%,#7cb0c8 55%,#2c3b24 75%,#0d130a 100%)}
.hero-title{left:296px;top:224px;font-family:"Cinzel",serif;color:var(--gold);line-height:1}
.hero-title .t1{display:block;font-size:21px}
.hero-title .t2{display:block;margin-top:10px;font-size:35px}
.hero-rule{left:296px;top:299px;width:210px;height:1px;background:#555}
.hero-author{left:296px;top:302px;width:212px;text-align:right;font-family:"Tinos",serif;font-weight:700;font-size:18px;color:var(--white)}
.hero-blurb{left:297px;top:338px;width:210px;font-size:8.5px;line-height:11.5px;color:var(--white)}
.read-more{left:296px;top:402px;width:100px;height:32px;border:1px solid var(--gold);display:flex}
.read-more span{flex:1;color:var(--gold);font-size:8.5px;font-weight:700;line-height:30px;padding-left:10px}
.read-more i{width:27px;background:var(--gold);display:flex;align-items:center;justify-content:center}

.section-head{font-family:"Arimo",Arial,sans-serif;font-size:11px;font-weight:400;color:var(--gold)}
.body-copy{font-size:8.5px;line-height:11.5px;color:var(--text)}
.chapter-label{left:422px;top:522px;font-size:9px;font-weight:700;color:#555;letter-spacing:.3px}
.continue{left:421px;top:602px;font-size:8.5px;color:#666;border-bottom:1px solid #888}

.author-band{left:0;top:660px;width:1200px;height:126px;background:var(--band)}
.avatar{left:296px;top:622px;width:100px;height:100px;border-radius:50%;border:2px solid #c8c8c8;background:linear-gradient(180deg,#d9d9d9 0%,#9a9a9a 45%,#1f2a33 100%)}

.quote-mark{left:422px;top:828px;font-family:"Tinos",serif;font-size:26px;color:#c4c4c4;line-height:1}
.quote{left:422px;top:852px;width:236px;font-size:8.5px;line-height:11.5px;font-style:italic;color:#777}
.quote-bar{left:422px;top:896px;width:234px;height:8px;background:#eeeeee}
.by{left:422px;top:914px;font-family:"Arimo",Arial,sans-serif;font-size:10.5px;color:#666}
.tweet-handle{left:714px;top:850px;display:flex;align-items:center;gap:8px;font-size:10px;color:#999}
.tweet-handle i{width:14px;height:14px;border-radius:50%;background:#9a9a9a}
.tweet{left:714px;width:182px;font-size:8.5px;line-height:11px;color:#444;font-weight:400}
.tweet a{color:var(--link);text-decoration:none}
.tweet small{font-size:6.5px;color:#888}

.footer-rule{left:297px;top:978px;width:600px;height:1px;background:var(--rule)}
.footer-note{top:988px;font-size:6.5px;color:#888}
</style>
</head>
<body>

<div class="abs top-bar"></div>
<div class="abs order">
  <svg width="17" height="14" viewBox="0 0 17 14" fill="none" stroke="#cfcfcf" stroke-width="1.3"><path d="M0 1h3l2 8h9l2-6H4"/><circle cx="6" cy="12" r="1.2"/><circle cx="13" cy="12" r="1.2"/></svg>
  <span>ORDER THIS BOOK <b>NOW!</b></span>
  <span class="vendor first">coinlet</span>
  <span class="vendor">vendoro</span>
</div>
<div class="abs social"><span>Chirpa</span><span>Vidra</span><span>Facely</span><span>Orbit</span></div>

<div class="abs masthead"></div>
<div class="abs site-name">Drifting Past Solvane</div>

<nav class="nav">
  <a class="active" href="#" style="left:440px">Home</a>
  <a href="#" style="left:497px">About Author</a>
  <a href="#" style="left:577px">Testimonial</a>
  <a href="#" style="left:660px">About Book</a>
  <a href="#" style="left:739px">Contact</a>
</nav>

<div class="abs hero"></div>
<div class="abs hero-art" role="img" aria-label="Book cover scene: a man's silhouette behind prison bars looking out at a tropical beach, a woman's legs in fishnet stockings at left"></div>
<div class="abs hero-title"><span class="t1">DRIFTING PAST</span><span class="t2">SOLVANE</span></div>
<div class="abs hero-rule"></div>
<div class="abs hero-author">Miles Harrow</div>
<p class="abs hero-blurb">Lorem Ipsum is simply dummy text of the printing and type-setting industry. Lorem Ipsum has been the industry's stan-dard dummy text ever since the 1500s</p>
<div class="abs read-more"><span>READ MORE</span><i><svg width="7" height="10" viewBox="0 0 7 10"><path d="M1 1l4 4-4 4" stroke="#000" stroke-width="2" fill="none"/></svg></i></div>

<h2 class="abs section-head" style="left:297px;top:520px">About Solvane</h2>
<div class="abs chapter-label">CHAPTER 1</div>
<p class="abs body-copy" style="left:422px;top:540px;width:478px">Lorem Ipsum is simply dummy text of the printing and typesetting industry. Lorem Ipsum has been the industry's standard dummy text ever since the 1500s, when an unknown printer took a galley of type and scrambled it to make a type specimen book.</p>
<p class="abs body-copy" style="left:422px;top:572px;width:478px">It has survived not only five centuries, but also the leap into electronic typesetting, remaining essentially unchanged. It was popularised in the 1960s with the release of Letraset sheets containing Lorem Ipsum passages</p>
<a class="abs continue">Continue &gt;&gt;</a>

<div class="abs author-band"></div>
<div class="abs avatar" role="img" aria-label="Portrait photo of the author in a dark suit"></div>
<h2 class="abs section-head" style="left:422px;top:683px">About Author</h2>
<p class="abs body-copy" style="left:422px;top:707px;width:478px">Lorem Ipsum is simply dummy text of the printing and typesetting industry. Lorem Ipsum has been the industry's standard dummy text ever since the 1500s, when an unknown printer took a galley of type and scrambled it to make a type specimen book.</p>
<p class="abs body-copy" style="left:422px;top:739px;width:478px">It has survived not only five centuries, but also the leap into electronic typesetting, remaining essentially unchanged. It was popularised in the 1960s.</p>

<h2 class="abs section-head" style="left:298px;top:831px">Testimonial</h2>
<div class="abs quote-mark">&ldquo;</div>
<p class="abs quote">Lorem Ipsum is simply dummy text of the printing and typesetting industry. Lorem Ipsum has been the industry's standard dummy text ever since the 1500s</p>
<div class="abs quote-bar"></div>
<svg class="abs" style="left:432px;top:903px" width="10" height="6"><path d="M0 0h10L5 6z" fill="#eeeeee"/></svg>
<div class="abs by">By Admin</div>

<h2 class="abs section-head" style="left:712px;top:831px">Get In Tweet</h2>
<div class="abs tweet-handle"><i></i>Drifting Past Solvane</div>
<p class="abs tweet" style="top:871px"><a>http://abc.solvane/</a>Lorem Ipsum is simply dummy text of the printing and typesetting industry <small>- 2min ago</small></p>
<p class="abs tweet" style="top:908px"><a>http://abc.solvane/</a>Lorem Ipsum is simply dummy text of the printing and typesetting industry <small>- 2min ago</small></p>

<div class="abs footer-rule"></div>
<div class="abs footer-note" style="left:297px">Copyright 2014 All Right Reserved. Company Name</div>

</body>
</html>
```